Business Card Design needed for logo design project

This project is linked to Consulting Firm + Meeting Space needs logo and bus card..
Our company needs a Business Card Design. Please refer to our original project in the link above.
Industry/Entity Type
Business

```html
<!DOCTYPE html>
<html lang="en">
<head>
<meta charset="utf-8">
<title>Harborline Business Card</title>
<link rel="stylesheet" href="https://fonts.googleapis.com/css2?family=Lato:wght@300;400;700;900&display=swap">
<style>
  :root {
    --stage: #2e2e2e;
    --card: #f7f7f7;
    --brand-blue: #1a6cc0;
    --name-blue: #12519a;
    --ink: #1f1f1f;
    --icon: #ffffff;
  }
  * { margin: 0; padding: 0; box-sizing: border-box; }
  html, body {
    width: 1200px;
    height: 997px;
    overflow: hidden;
    background: var(--stage);
    font-family: "Lato", sans-serif;
  }
  .card {
    position: absolute;
    left: 280px;
    width: 640px;
    height: 366px;
    background: var(--card);
    overflow: hidden;
  }
  .card--back { top: 70px; }
  .card--front { top: 540px; }
  .card__bands {
    position: absolute;
    inset: 0;
    width: 100%;
    height: 100%;
  }
  .band { fill: var(--brand-blue); }
  .wordmark {
    position: absolute;
    font-family: "Lato", sans-serif;
    font-weight: 300;
    color: var(--brand-blue);
    letter-spacing: 1px;
    line-height: 1;
  }
  .card--back .wordmark {
    left: 0; right: 0;
    top: 145px;
    text-align: center;
    font-size: 72px;
  }
  .card--front .wordmark {
    left: 60px;
    top: 60px;
    font-size: 72px;
  }
  .holder {
    position: absolute;
    right: 32px;
    top: 152px;
    text-align: right;
  }
  .holder__name {
    font-weight: 900;
    font-size: 21px;
    color: var(--name-blue);
    letter-spacing: 0.3px;
  }
  .holder__role {
    font-weight: 400;
    font-size: 15px;
    color: var(--ink);
  }
  .contacts {
    position: absolute;
    left: 40px;
    top: 262px;
    list-style: none;
  }
  .contacts li {
    font-weight: 700;
    font-size: 15px;
    color: var(--ink);
    height: 30px;
    line-height: 30px;
  }
  .icon { fill: none; stroke: var(--icon); stroke-width: 1.4; }
  .icon--solid { fill: var(--icon); stroke: none; }
</style>
</head>
<body>

<section class="card card--back" aria-label="Card back">
  <svg class="card__bands" viewBox="0 0 640 366" aria-hidden="true">
    <path class="band" d="M0 0 H300 Q285 0 270 8 H0 Z"/>
    <path class="band" d="M640 366 H330 Q345 366 360 356 H640 Z"/>
  </svg>
  <div class="wordmark">Harborline</div>
</section>

<section class="card card--front" aria-label="Card front">
  <svg class="card__bands" viewBox="0 0 640 366" aria-hidden="true">
    <path class="band" d="M640 0 H240 Q228 0 215 9 H640 Z"/>
    <path class="band" d="M640 366 H340 Q355 366 370 356 H640 Z"/>
    <rect class="band" x="618" y="156" width="30" height="32" rx="5"/>
    <path class="band" d="M0 246 H18 Q26 246 26 254 V344 Q26 352 18 352 H0 Z"/>
    <g transform="translate(13 277)">
      <path class="icon--solid" d="M-6 -2 Q-6 -6 0 -6 Q6 -6 6 -2 L4 -1 L3 -3 H-3 L-4 -1 Z M-4 0 H4 L5 5 H-5 Z"/>
    </g>
    <g transform="translate(13 306)">
      <rect class="icon" x="-3.5" y="-6" width="7" height="12" rx="1"/>
    </g>
    <g transform="translate(13 335)">
      <rect class="icon" x="-6" y="-4" width="12" height="8"/>
      <path class="icon" d="M-6 -4 L0 1 L6 -4"/>
    </g>
  </svg>
  <div class="wordmark">Harborline</div>
  <div class="holder">
    <div class="holder__name">MARISSA DALTON</div>
    <div class="holder__role">Account Manager</div>
  </div>
  <ul class="contacts">
    <li>555-318-2040</li>
    <li>555-472-9163</li>
    <li>mdalton@northfieldgroup.com</li>
  </ul>
</section>

</body>
</html>
```